Coastal Pulse Fiesta wordpress website

We need a wordpress design for a Brazilian dance festival event to happen in mid August in Sydney Australia.

The elevator pitch for this event is:

"Coastal Pulse Fiest is for the Social dancer who loves Brazilian rhythms and wants to have a space to dance, socialize and be inspired by a more intense experience than a regular class. As opposed to congress & festivals where there is a formality and focus on performances our events focus on relaxed and warm interactions between dance professionals and dance amateurs."

Most dances are originally from Rio de Janeiro-Brazil and we want to emphasize the cultural connection between both cities Rio (Brazil) & Sydney (Australia): beach culture, warm smiley people, love for music, dance and outdoors.

Feel free to contrast flag colours red/white/blue (Australia) & Green/yellow (Brazil)

We do not have a logo and the template / theme will be hosted on Wordpress 3.5.2
Updates

Project Deadline Extended
Reason: We still havent found anything we like and some professionals have asked more time to provide a 2nd design.

Hi everyone,

Just to let you know we've extended the deadline on this design project.

Good luck

Hi please

1. use the three uploaded pics of couples dancing as a primary feature in a banner across the page.
2. use the colours of brazil - greens, yellows and blues where possible if you have not used already.
3. Do the Heart in We Sway Tropic Dance as an actual heart image.

Thanks, looking forward to the revisions.

Cheers

Marcelo and Lucy

Target Market(s)

social dancers- men & women between 25 and 60 yo. The majority of participants are single.

Industry/Entity Type

Festival

Requirements
Must have
• Top menu to be editable via wordpress.
Nice to have
• The theme should be up, lively and fun, yet relaxed and informal.
Should not have
• Any images / sillouettes of samba Carnival women in Feathers.

```html
<!DOCTYPE html>
<html lang="en">
<head>
<meta charset="utf-8">
<title>Coastal Pulse Fiesta – Social Dance Festival</title>
<link rel="stylesheet" href="https://fonts.googleapis.com/css2?family=Arvo:ital,wght@1,400;1,700&family=Lato:wght@400;700&family=Montserrat:wght@300;500;600;700&family=Open+Sans:wght@400&display=swap">
<style>
  :root {
    --header-red: #a8121b;
    --header-red-deep: #8c0d15;
    --logo-tint: #d9737a;
    --nav-black: #0b0b0b;
    --nav-text: #d8d8d8;
    --nav-divider: #444444;
    --cream: #fdf6cf;
    --ink: #1a1a1a;
    --body-ink: #3c3c3c;
    --stripe-blue: #1d3f96;
    --stripe-yellow: #f4c312;
    --stripe-green: #149a48;
    --book-ring: #f1b28c;
    --book-ring-outer: #f6d2b4;
    --book-border: #e58c6a;
    --book-red: #b81d22;
    --social-dark: #6e1010;
    --white: #ffffff;
    --date-pink: #e7a4d8;
    --year-lilac: #c9b0e0;
  }
  * { box-sizing: border-box; margin: 0; padding: 0; }
  html, body { width: 1200px; height: 1200px; overflow: hidden; background: var(--white); }
  .canvas { position: relative; width: 1200px; height: 1200px; overflow: hidden; background: var(--cream); font-family: "Open Sans", sans-serif; }

  /* Header */
  .site-header { position: absolute; left: 0; top: 0; width: 1200px; height: 145px;
    background: linear-gradient(180deg, var(--header-red) 0%, var(--header-red-deep) 100%); }
  .brand { position: absolute; left: 107px; top: 12px; display: flex; align-items: center; gap: 18px; }
  .brand-square { width: 93px; height: 113px; background: var(--logo-tint); }
  .brand-name { font-family: "Montserrat", sans-serif; font-weight: 500; color: var(--white);
    font-size: 35px; line-height: 35px; letter-spacing: 1px; text-transform: uppercase; }

  .flag-band { position: absolute; left: 0; width: 1200px; height: 12px; display: flex; flex-direction: column; }
  .flag-band span { flex: 1; }
  .flag-band .b { background: var(--stripe-blue); }
  .flag-band .y { background: var(--stripe-yellow); }
  .flag-band .g { background: var(--stripe-green); }
  .flag-band.top { top: 145px; }
  .flag-band.bottom { top: 1130px; }

  /* Navigation */
  .main-nav { position: absolute; left: 0; top: 157px; width: 1200px; height: 55px; background: var(--nav-black); }
  .main-nav ul { list-style: none; display: flex; align-items: center; height: 55px; padding-left: 110px; }
  .main-nav li { font-family: "Lato", sans-serif; font-size: 15px; color: var(--nav-text);
    text-transform: uppercase; padding: 0 20px; border-left: 1px solid var(--nav-divider); line-height: 18px; }
  .main-nav li:first-child { border-left: none; padding-left: 0; color: var(--white); font-weight: 700; }

  /* Hero */
  .hero { position: absolute; left: 0; top: 212px; width: 1200px; height: 490px; }
  .hero-photo { position: absolute; inset: 0;
    background:
      radial-gradient(ellipse 320px 200px at 620px 120px, rgba(200,40,90,0.55), transparent 70%),
      radial-gradient(ellipse 260px 260px at 900px 330px, rgba(120,60,170,0.45), transparent 70%),
      radial-gradient(ellipse 400px 160px at 600px 420px, rgba(230,120,60,0.35), transparent 70%),
      linear-gradient(180deg, #1c0d14 0%, #2a1420 55%, #3a1a22 100%); }
  .hero-stripes { position: absolute; left: 0; top: 110px; width: 420px; height: 380px; }
  .hero-title { position: absolute; right: 112px; top: 130px; text-align: right; color: var(--white); font-family: "Montserrat", sans-serif; }
  .hero-title .line-1 { display: block; font-weight: 600; font-size: 62px; line-height: 66px; letter-spacing: 1px; }
  .hero-title .line-2 { display: block; font-weight: 300; font-size: 44px; line-height: 54px; letter-spacing: 1px; }
  .hero-date { position: absolute; right: 112px; top: 252px; width: 590px; font-family: "Montserrat", sans-serif; font-weight: 700; text-align: right; }
  .hero-date .day-month { color: var(--date-pink); font-size: 98px; line-height: 100px; letter-spacing: 2px; }
  .hero-date .year { color: var(--year-lilac); font-size: 132px; line-height: 116px; letter-spacing: 4px; text-align: center; padding-left: 60px; }
  .hero-edge { position: absolute; left: 0; top: 672px; width: 1200px; height: 30px; }

  /* Content */
  .intro { position: absolute; left: 100px; top: 748px; width: 715px; }
  .intro-title { font-family: "Arvo", serif; font-style: italic; font-weight: 700; font-size: 36px; line-height: 44px; color: var(--ink); }
  .intro-subtitle { font-family: "Arvo", serif; font-style: italic; font-weight: 400; font-size: 26px; line-height: 36px; color: var(--ink); margin-top: 4px; }
  .intro-body { font-size: 13px; line-height: 16px; color: var(--body-ink); margin-top: 22px; }

  .book-badge { position: absolute; left: 818px; top: 700px; width: 226px; height: 226px; border-radius: 50%;
    background: var(--book-ring-outer); display: flex; align-items: center; justify-content: center; }
  .book-badge .ring { width: 196px; height: 196px; border-radius: 50%; background: var(--book-ring);
    display: flex; align-items: center; justify-content: center; }
  .book-badge .core { width: 158px; height: 158px; border-radius: 50%; background: var(--cream);
    border: 4px solid var(--book-border); display: flex; flex-direction: column; align-items: center; justify-content: center; text-align: center; }
  .book-badge .cta { font-family: "Arvo", serif; font-style: italic; font-weight: 700; color: var(--book-red); font-size: 26px; line-height: 28px; }
  .book-badge .note { font-family: "Arvo", serif; font-style: italic; font-size: 15px; line-height: 18px; color: var(--ink); margin-top: 4px; }
  .book-badge .note em { color: var(--book-red); font-style: italic; }

  .social-links { position: absolute; left: 850px; top: 938px; display: flex; gap: 14px; }
  .social-links span { width: 46px; height: 46px; border-radius: 50%; background: var(--social-dark); display: block; }

  .crowd-photo { position: absolute; left: 0; top: 990px; width: 1200px; height: 140px;
    background: linear-gradient(180deg, var(--cream) 0%, #d9a37a 35%, #8a3a26 70%, #4a1a14 100%); }

  /* Footer */
  .site-footer { position: absolute; left: 0; top: 1142px; width: 1200px; height: 58px; background: var(--header-red);
    display: flex; align-items: center; padding-left: 108px; }
  .site-footer p { font-family: "Lato", sans-serif; font-size: 14px; color: var(--white); text-transform: uppercase; letter-spacing: 0.5px; }
  .site-footer .sep { margin: 0 14px; }
</style>
</head>
<body>
<div class="canvas">

  <header class="site-header">
    <div class="brand">
      <span class="brand-square"></span>
      <span class="brand-name">Coastal<br>Pulse<br>Fiesta</span>
    </div>
  </header>
  <div class="flag-band top"><span class="b"></span><span class="y"></span><span class="g"></span></div>

  <nav class="main-nav">
    <ul>
      <li>Home</li>
      <li>Event Information</li>
      <li>Instructor Profiles</li>
      <li>Timetable</li>
      <li>Tickets</li>
      <li>About Us</li>
      <li>Contact Us</li>
    </ul>
  </nav>

  <section class="hero">
    <div class="hero-photo" role="img" aria-label="Festival stage at night with coloured lights above a dancing crowd"></div>
    <svg class="hero-stripes" viewBox="0 0 420 380" role="img" aria-label="Diagonal bands in Brazilian and Australian colours">
      <defs>
        <linearGradient id="band-tones" x1="0" y1="0" x2="1" y2="1">
          <stop offset="0" stop-color="#d3241d"/>
          <stop offset="0.35" stop-color="#e9831f"/>
          <stop offset="0.6" stop-color="#149a48"/>
          <stop offset="1" stop-color="#1d3f96"/>
        </linearGradient>
      </defs>
      <polygon points="0,0 420,380 250,380 0,150" fill="url(#band-tones)"/>
    </svg>
    <h1 class="hero-title">
      <span class="line-1">HARBOUR SAMBA</span>
      <span class="line-2">SOCIAL DANCE FESTIVAL</span>
    </h1>
    <div class="hero-date">
      <div class="day-month">16 AUGUST</div>
      <div class="year">2014</div>
    </div>
  </section>
  <svg class="hero-edge" viewBox="0 0 1200 30" preserveAspectRatio="none">
    <polygon fill="#fdf6cf" points="0,30 0,14 20,4 40,14 60,4 80,14 100,4 120,14 140,4 160,14 180,4 200,14 220,4 240,14 260,4 280,14 300,4 320,14 340,4 360,14 380,4 400,14 420,4 440,14 460,4 480,14 500,4 520,14 540,4 560,14 580,4 600,14 620,4 640,14 660,4 680,14 700,4 720,14 740,4 760,14 780,4 800,14 820,4 840,14 860,4 880,14 900,4 920,14 940,4 960,14 980,4 1000,14 1020,4 1040,14 1060,4 1080,14 1100,4 1120,14 1140,4 1160,14 1180,4 1200,14 1200,30"/>
  </svg>

  <section class="intro">
    <h2 class="intro-title">Lorem ipsum dolor sit amet</h2>
    <p class="intro-subtitle">consectetuer adipiscing elit</p>
    <p class="intro-body">Join us for a weekend of relaxed social dancing, open floors and warm company. Our teachers share simple ideas you can use straight away, then the music takes over until late. Come alone or with friends, bring comfy shoes and a smile, and meet dancers from every corner of the city. Beginners are welcome at every session, and the friendly crew is always on hand to help you find a partner and settle into the groove on the beach side of town tonight.</p>
  </section>

  <aside class="book-badge">
    <div class="ring">
      <div class="core">
        <span class="cta">Book<br>Now!</span>
        <span class="note">Jump straight<br>in to<br><em>book online!</em></span>
      </div>
    </div>
  </aside>

  <div class="social-links" aria-label="Social links">
    <span></span><span></span><span></span>
  </div>

  <div class="crowd-photo" role="img" aria-label="Crowd of dancers with raised hands under warm lights"></div>

  <div class="flag-band bottom"><span class="b"></span><span class="y"></span><span class="g"></span></div>
  <footer class="site-footer">
    <p>©2014 Coastal Pulse Fiesta<span class="sep">|</span>All rights reserved</p>
  </footer>

</div>
</body>
</html>
```